Email marketing for Larkfield Ophthalmic Services

I need nice design brochure for e mail marketing telling my customers our services and products, location, etc.
At Larkfield Ophthalmic Services, we have 25 plus years of combined experience servicing ophthalmic equipment. We offer reliable, timely and economic repairs of a variety of new and discontinued equipment, including, but not limited to Exam Chairs and Stands, Phoropters, Slit Lamps, Keratometers, Hand-helds, BIO’s, Auto Lensmeters, AutoRefractors, Non-Contact Tonometers, Goldman Tonometers, Vira-Dots and many more.

We service all major brands such as: Vemmo Brisk, Pelno, Wexlan, Durovane, Falkonz, Brastee, Quenby and more.
We do Preventative Maintenance, Practice Moving, Office Relocation Consulting, Layout Strategy and Equipment Set Up Solutions.

Target Market(s)

Optometrist, Ophthalmologists, Optical Stores

Font styles to use
Sans Serif

Colors
34a6d7

Requirements
Must have
• We comply with all the safety measure according to QPV. Emphasize more on services, service calls.
Link to my website www.larkfieldophthalmic-svc.example
We buy, sale and service ophthalmic equipment.
Phoroptor cleaning only 275.00. Please use file 4.
File 3 special price for a limited time 925.00.
File 1, Refractor Breath Shield- 19.00.
File 2, Slit Lamp Breath Shield XL 17.00
Nice to have
• I want nice looking professional design that also assures my customers that we are open for business, we comply with all the safety guidelines.

```html
<!DOCTYPE html>
<html lang="en">
<head>
<meta charset="utf-8">
<title>Larkfield Ophthalmic Services – Flyer</title>
<link rel="stylesheet" href="https://fonts.googleapis.com/css2?family=Barlow:wght@400;500;600;700&display=swap">
<style>
  :root{
    --navy:#2b3478;
    --ink:#23222f;
    --slate:#55595e;
    --cyan:#4ab8da;
    --white:#ffffff;
    --price:#ffe600;
    --page:#e9eaec;
  }
  *{margin:0;padding:0;box-sizing:border-box}
  html,body{width:977px;height:1200px;overflow:hidden;background:var(--page)}
  body{font-family:"Barlow",Arial,sans-serif;position:relative}
  .flyer{position:absolute;left:26px;top:0;width:924px;height:1200px;background:var(--white);overflow:hidden}
  .shapes{position:absolute;left:0;top:0}
  .logo{position:absolute;left:48px;top:50px;display:flex;align-items:center;gap:10px;color:var(--white);font-weight:500;text-transform:uppercase;line-height:1.05}
  .logo-dot{width:30px;height:30px;border-radius:50%;background:var(--cyan);flex:none}
  .logo-name{font-size:30px;letter-spacing:1px}
  .logo-name small{display:block;font-size:30px;letter-spacing:8px;padding-left:104px}
  .address{position:absolute;right:32px;top:64px;text-align:right;color:var(--white);font-weight:600;font-size:18px;line-height:25px}
  .website{position:absolute;left:62px;top:180px;color:var(--white);font-weight:700;font-size:18px}
  .hero-photo{position:absolute;left:0;top:237px;width:560px;height:329px;
    background:linear-gradient(90deg,rgba(255,255,255,0) 60%,#fff 100%),
    radial-gradient(circle at 8% 5%,#f3a06a 0,rgba(243,160,106,0) 22%),
    linear-gradient(135deg,#8fb3de 0%,#2c4f8a 40%,#6e92c8 70%,#d8e4f4 100%)}
  .headline{position:absolute;right:32px;top:236px;text-align:right;color:var(--navy);font-weight:700;font-size:61px;line-height:75px;letter-spacing:.5px;text-transform:uppercase}
  .about{position:absolute;left:0;top:566px;width:924px;padding:22px 32px 0 42px;color:var(--white);font-size:16.2px;line-height:21.8px}
  .about p{text-align:justify;margin-bottom:21.8px}
  .phone{position:absolute;right:34px;top:790px;display:flex;align-items:center;gap:14px;color:var(--white);font-weight:700;font-size:37px;letter-spacing:1px;line-height:46px}
  .phone svg{width:38px;height:38px}
  .safety{position:absolute;left:42px;top:826px;width:250px;color:var(--navy);font-weight:600;font-size:14px;line-height:18px}
  .offers{position:absolute;left:45px;top:908px;display:flex;gap:11px}
  .offer{width:201px;height:244px;border:2px solid var(--navy);border-radius:10px;background:var(--navy);overflow:hidden;text-align:center;color:var(--white)}
  .offer-photo{height:150px;border-radius:8px 8px 0 0}
  .offer-title{font-weight:700;font-size:17px;line-height:22px;margin-top:11px;text-transform:uppercase}
  .offer-note{font-weight:700;font-size:17px;line-height:22px}
  .offer-price{font-weight:700;font-size:31px;line-height:30px;color:var(--price)}
  .p1{background:linear-gradient(160deg,#f2f2f2,#9a9a9e 55%,#ececec)}
  .p2{background:linear-gradient(180deg,#fafafa,#e6e6e6)}
  .p3{background:linear-gradient(180deg,#5f5a55,#cfc9c0 50%,#3e3a36)}
  .p4{background:linear-gradient(90deg,#8a8478,#d9cdb8 55%,#b8ab95)}
</style>
</head>
<body>
<div class="flyer">
  <svg class="shapes" width="924" height="1200" viewBox="0 0 924 1200" aria-hidden="true">
    <rect x="0" y="0" width="924" height="190" fill="var(--navy)"/>
    <polygon points="0,148 530,148 556,118 609,190 410,190 370,237 0,237" fill="var(--ink)"/>
    <polygon points="487,118 556,118 452,207 383,207" fill="var(--slate)"/>
    <rect x="0" y="566" width="924" height="247" fill="var(--navy)"/>
    <polygon points="559,767 924,767 924,856 460,856 365,885 306,813 508,813" fill="var(--cyan)"/>
    <polygon points="451,798 527,798 443,885 364,885" fill="var(--slate)"/>
  </svg>

  <div class="logo">
    <span class="logo-dot"></span>
    <span class="logo-name">Larkfield Ophthalmic<small>Services</small></span>
  </div>
  <div class="address">1480 Alder Row<br>Fernbrook, IL 60099</div>
  <div class="website">www.larkfieldophthalmic-svc.example</div>

  <div class="hero-photo" role="img" aria-label="Close-up photo of a slit lamp microscope in an eye exam room"></div>
  <h1 class="headline">We buy, sale<br>and service<br>ophthalmic<br>equipment</h1>

  <section class="about">
    <p>At Larkfield Ophthalmic Services, we have 25 plus years of combined experience servicing ophthalmic equipment. We offer reliable, timely and economic repairs of a variety of new and discontinued equipment, including, but not limited to Exam Chairs and Stands, Phoropters, Slit Lamps, Keratometers, Hand-helds, BIO’s, Auto Lensmeters, AutoRefractors, Non-Contact Tonometers, Goldman Tonometers, Vira-Dots and many more.</p>
    <p>We service all major brands such as: Vemmo Brisk, Pelno, Wexlan, Durovane, Falkonz, Brastee, Quenby and more. We do Preventative Maintenance, Practice Moving, Office Relocation Consulting, Layout Strategy and Equipment Set Up Solutions.</p>
  </section>

  <div class="phone">
    <svg viewBox="0 0 40 40" aria-hidden="true"><circle cx="20" cy="20" r="19" fill="var(--white)"/><path d="M14 10c1-.6 2.2-.3 2.8.7l2 3.4c.5.9.3 2-.5 2.6l-1.4 1c.9 2.3 2.6 4.2 4.8 5.4l1.1-1.3c.7-.8 1.8-1 2.7-.4l3.3 2.2c1 .6 1.2 1.9.6 2.8l-1.2 1.7c-.8 1.1-2.2 1.6-3.5 1.2C18.6 27.5 12.6 21.4 11 15.2c-.3-1.3.2-2.7 1.3-3.5z" fill="var(--cyan)"/></svg>
    <span>555-014-2738</span>
  </div>

  <p class="safety">We are open for business and comply with all QPV safety guidelines.</p>

  <div class="offers">
    <article class="offer">
      <div class="offer-photo p1" role="img" aria-label="Photo of disassembled phoropter parts"></div>
      <div class="offer-title">Phoroptor cleaning</div>
      <div class="offer-note">only</div>
      <div class="offer-price">275.00</div>
    </article>
    <article class="offer">
      <div class="offer-photo p2" role="img" aria-label="Photo of a visual acuity monitor with remote"></div>
      <div class="offer-title">Special price</div>
      <div class="offer-note">for a limited time</div>
      <div class="offer-price">925.00</div>
    </article>
    <article class="offer">
      <div class="offer-photo p3" role="img" aria-label="Photo of a refractor fitted with a breath shield"></div>
      <div class="offer-title">Refractor<br>breath shield</div>
      <div class="offer-price">19.00</div>
    </article>
    <article class="offer">
      <div class="offer-photo p4" role="img" aria-label="Photo of a slit lamp with an XL breath shield"></div>
      <div class="offer-title">Slit lamp<br>breath shield XL</div>
      <div class="offer-price">17.00</div>
    </article>
  </div>
</div>
</body>
</html>
```